Kestrel Facility Systems needs a business card design with logo

need a business card and log design for a company called "Kestrel Facility Systems". we improve building energy efficiency and save energy costs through building automation systems for commercial buildings such as hospitals, office buildings, universities, etc. The final design should communicate elements such as "precision", "energy efficiency", "green buildings". back side should list our service offerings

```html
<!DOCTYPE html>
<html lang="en">
<head>
<meta charset="utf-8">
<title>Kestrel Facility Systems — Business Card</title>
<link href="https://fonts.googleapis.com/css2?family=Montserrat:wght@400;500;700;800&display=swap" rel="stylesheet">
<style>
  :root {
    --page: #ececec;
    --card-light: #f6f6f6;
    --card-dark: #2b2b2b;
    --green: #4cae3c;
    --ink: #2f2f2f;
    --ink-soft: #4a4a4a;
    --rule: #b9b9b9;
    --on-dark: #e6e6e6;
  }
  * { box-sizing: border-box; margin: 0; padding: 0; }
  html, body { width: 1200px; height: 1138px; overflow: hidden; }
  body {
    background: var(--page);
    font-family: "Montserrat", Arial, sans-serif;
    display: flex;
    flex-direction: column;
    align-items: center;
    justify-content: center;
    gap: 60px;
  }
  .card {
    width: 840px;
    height: 480px;
    box-shadow: 0 6px 24px rgba(0,0,0,0.12);
    position: relative;
  }
  .brand {
    display: flex;
    align-items: center;
    gap: 18px;
  }
  .brand-dot {
    width: 54px; height: 54px;
    border-radius: 50%;
    background: var(--green);
    flex: none;
  }
  .brand-name {
    color: var(--green);
    font-weight: 800;
    font-size: 30px;
    line-height: 1.1;
    letter-spacing: 0.5px;
    text-transform: uppercase;
  }

  /* back */
  .card-back {
    background: var(--card-dark);
    display: flex;
    flex-direction: column;
    align-items: center;
    justify-content: center;
    gap: 40px;
  }
  .services {
    color: var(--on-dark);
    font-weight: 500;
    font-size: 17px;
    letter-spacing: 1.5px;
    text-align: center;
    line-height: 1.6;
  }

  /* front */
  .card-front {
    background: var(--card-light);
    display: grid;
    grid-template-columns: 1fr 1px 1fr;
    align-items: center;
  }
  .card-front .brand { justify-self: center; }
  .card-front .brand-name { font-size: 26px; }
  .divider {
    width: 1px; height: 220px;
    background: var(--rule);
  }
  .contact { padding-left: 44px; color: var(--ink-soft); }
  .contact-name {
    font-weight: 800;
    font-size: 26px;
    color: var(--ink);
    letter-spacing: 0.5px;
  }
  .contact-title { font-size: 15px; margin-top: 2px; }
  .contact-address { font-size: 15px; margin-top: 14px; line-height: 1.45; }
  .contact-lines { list-style: none; margin-top: 14px; font-size: 15px; }
  .contact-lines li {
    display: flex; align-items: center; gap: 10px;
    line-height: 1.55;
  }
  .contact-lines svg { width: 14px; height: 14px; flex: none; }
</style>
</head>
<body>

  <section class="card card-back">
    <div class="brand">
      <span class="brand-dot"></span>
      <span class="brand-name">Kestrel Facility Systems</span>
    </div>
    <p class="services">
      SERVICES • SERVICES • SERVICES<br>
      SERVICES • SERVICES
    </p>
  </section>

  <section class="card card-front">
    <div class="brand">
      <span class="brand-dot"></span>
      <span class="brand-name">Kestrel Facility<br>Systems</span>
    </div>
    <span class="divider"></span>
    <div class="contact">
      <h1 class="contact-name">Daniel REEVE</h1>
      <p class="contact-title">Managing Director</p>
      <p class="contact-address">418 Harrow Line Rd 7 East<br>Millbrook ON, Canada, L0A 1G0</p>
      <ul class="contact-lines">
        <li>
          <svg viewBox="0 0 16 16" aria-hidden="true"><path d="M4 1.5l2.5 3-1.5 1.7a8 8 0 0 0 4.8 4.8L11.5 9.5l3 2.5-1.6 2.3C7 14 2 9 1.7 3.1z" fill="var(--green)"/></svg>
          000.000.0000
        </li>
        <li>
          <svg viewBox="0 0 16 16" aria-hidden="true"><rect x="4" y="1.5" width="8" height="13" rx="1.5" fill="none" stroke="var(--green)" stroke-width="1.6"/></svg>
          000.000.0000
        </li>
        <li>
          <svg viewBox="0 0 16 16" aria-hidden="true"><rect x="1.5" y="3.5" width="13" height="9" fill="none" stroke="var(--green)" stroke-width="1.5"/><path d="M1.5 3.5L8 9l6.5-5.5" fill="none" stroke="var(--green)" stroke-width="1.5"/></svg>
          daniel@kestrelfacility.com
        </li>
        <li>
          <svg viewBox="0 0 16 16" aria-hidden="true"><g fill="none" stroke="var(--green)" stroke-width="1.3"><circle cx="8" cy="8" r="6.5"/><ellipse cx="8" cy="8" rx="3" ry="6.5"/><path d="M1.5 8h13M2.5 4.8h11M2.5 11.2h11"/></g></svg>
          www.kestrelfacility.com
        </li>
      </ul>
    </div>
  </section>

</body>
</html>
```